" Quintela advogados é um escritório de advocacia de grande porte atuando em 6 Estados, sendo em 3 deles temos filial em funcionamento, além da matriz (Curitiba). "

```html
<!DOCTYPE html>
<html lang="pt-BR">
<head>
<meta charset="utf-8">
<title>Quintela Advogados — Bloco de notas</title>
<link rel="stylesheet" href="https://fonts.googleapis.com/css2?family=Cinzel:wght@500&family=Open+Sans:wght@400&display=swap">
<style>
  :root{
    --backdrop:#e7e2dc;
    --navy-top:#233243;
    --navy-bottom:#0c1520;
    --paper:#ffffff;
    --ink:#1e2a36;
    --gold:#c9a063;
    --gold-soft:#e4c99a;
    --watermark:#e6e6e6;
    --text-muted:#555c63;
  }
  *{box-sizing:border-box;margin:0;padding:0}
  html,body{width:1200px;height:1200px;overflow:hidden;background:var(--backdrop)}
  .canvas{position:relative;width:1200px;height:1200px}

  .notepad{position:absolute;width:372px;height:521px;overflow:hidden;
    box-shadow:0 10px 22px rgba(0,0,0,.18)}
  .notepad--cover{left:211px;top:43px;
    background:linear-gradient(160deg,var(--navy-top),var(--navy-bottom))}
  .notepad--letterhead{left:612px;top:43px;background:var(--paper)}
  .notepad--blank{left:420px;top:600px;width:380px;height:523px;background:var(--paper)}

  .binding-holes{position:absolute;top:6px;left:0;right:0;display:flex;justify-content:center;gap:10px}
  .binding-holes span{width:20px;height:20px;border-radius:50%;background:var(--backdrop)}

  .brand{position:absolute;left:0;right:0;text-align:center;font-family:"Cinzel",serif;font-weight:500}
  .brand__mark{display:block;margin:0 auto;transform:rotate(45deg)}
  .brand__name{display:block;letter-spacing:.08em;line-height:1}
  .brand__tag{display:block;letter-spacing:.45em;line-height:1}

  .notepad--cover .brand{top:200px;color:var(--paper)}
  .notepad--cover .brand__mark{width:62px;height:62px;border:4px solid var(--gold);margin-bottom:34px}
  .notepad--cover .brand__name{font-size:40px}
  .notepad--cover .brand__tag{font-size:11px;margin-top:8px;padding-left:.45em}

  .notepad--letterhead .brand{top:54px;color:var(--ink)}
  .notepad--letterhead .brand__mark{width:30px;height:30px;border:3px solid var(--ink);margin-bottom:16px}
  .notepad--letterhead .brand__name{font-size:22px}
  .notepad--letterhead .brand__tag{font-size:6px;margin-top:4px;padding-left:.45em}

  .watermark{position:absolute;left:50%;width:180px;height:180px;margin-left:-90px;
    border:14px solid var(--watermark);transform:rotate(45deg)}
  .notepad--letterhead .watermark{top:170px}
  .notepad--blank .watermark{top:200px}

  .contact{position:absolute;left:0;right:0;top:478px;text-align:center;
    font-family:"Open Sans",sans-serif;font-size:9.5px;line-height:1.45;color:var(--text-muted)}

  .footer-band{position:absolute;left:0;right:0;bottom:0;height:38px;
    background:linear-gradient(180deg,var(--navy-top),var(--navy-bottom))}
  .footer-rule{position:absolute;left:0;right:0;bottom:48px;height:2px;
    background:linear-gradient(90deg,transparent,var(--gold-soft),transparent)}
</style>
</head>
<body>
<main class="canvas">

  <section class="notepad notepad--cover">
    <div class="binding-holes"><span></span><span></span><span></span><span></span><span></span><span></span><span></span><span></span><span></span><span></span><span></span></div>
    <div class="brand">
      <span class="brand__mark"></span>
      <span class="brand__name">QUINTELA</span>
      <span class="brand__tag">ADVOGADOS</span>
    </div>
  </section>

  <section class="notepad notepad--letterhead">
    <div class="binding-holes"><span></span><span></span><span></span><span></span><span></span><span></span><span></span><span></span><span></span><span></span><span></span></div>
    <div class="brand">
      <span class="brand__mark"></span>
      <span class="brand__name">QUINTELA</span>
      <span class="brand__tag">ADVOGADOS</span>
    </div>
    <div class="watermark"></div>
    <address class="contact" style="font-style:normal">
      +55 41 3020-4455<br>
      R. Marechal, Nº 120 - Curitiba - PR<br>
      contato@quintela.com.br
    </address>
  </section>

  <section class="notepad notepad--blank">
    <div class="binding-holes"><span></span><span></span><span></span><span></span><span></span><span></span><span></span><span></span><span></span><span></span><span></span></div>
    <div class="watermark"></div>
    <div class="footer-rule"></div>
    <div class="footer-band"></div>
  </section>

</main>
</body>
</html>
```